New Zealand Costume Website

Hello,

I am building a costume website for New Zealand. I have a template design in place, which I'm happy with but I require the design to be tidied up. For example, the design of banners, logo and general look and feel. I am happy with the layout of the website so it's really just the graphics/banners that need designing.

I need the design to reflect the NZ market so I'd like designs that use the Kiwi bird, which can be seen in the successful pivalo.co.nz website. The design should be fun and geared towards children.

The URL of the site is brindlehop.co.nz.

Thanks,

Oliver.

Reason: Apologies, I need to fill the site with content. Will take about 4 days. This will help u design the site.

Target Market(s)

Parents looking to buy fancy dress costumes for their children.

Requirements
Nice to have
• Ecommerce website design experience

```html
<!DOCTYPE html>
<html lang="en">
<head>
<meta charset="utf-8">
<title>Kids Costumes – brindlehop.co.nz</title>
<link href="https://fonts.googleapis.com/css2?family=Arvo:wght@400;700&family=Arimo:wght@400;700&display=swap" rel="stylesheet">
<style>
:root{
  --plum:#9a2f66;
  --plum-dark:#7e2453;
  --berry:#c0396f;
  --coral:#ef5a5c;
  --coral-dark:#d94549;
  --orange:#f7931e;
  --red-pink:#ee3b5b;
  --amber:#fbb116;
  --yellow:#ffd200;
  --cream:#f4f1e8;
  --paper:#fbf9f3;
  --tan:#c49b73;
  --tan-light:#d9bc98;
  --cloud:#ebe7d8;
  --ink:#222;
  --grey-band:#d7d8cd;
  --stock:#b72d5f;
}
*{box-sizing:border-box;margin:0;padding:0}
html,body{width:1200px;height:2167px;overflow:hidden}
body{background:var(--cream);font-family:Arimo,Arial,sans-serif;color:var(--ink);position:relative}
.edge-band{position:absolute;left:0;width:1200px;height:7px;
  background:linear-gradient(90deg,#e06a95,#a8c56b 30%,#f3a955 55%,#6bb9dd 80%,#b05a88)}
/* header */
.header{position:absolute;top:0;left:0;width:1200px;height:88px;background:var(--paper)}
.brand{position:absolute;left:172px;top:24px;display:flex;align-items:center;gap:12px}
.brand-dot{width:48px;height:48px;border-radius:50%;background:var(--plum)}
.brand-name{font:700 30px/1 Arimo,Arial,sans-serif;color:var(--ink)}
.brand-tag{font:400 12px Arimo,Arial,sans-serif;color:#444;margin-top:4px}
.top-links{position:absolute;right:176px;top:17px;display:flex;gap:14px;font:700 11px Arimo,Arial,sans-serif;color:#333}
.badges{position:absolute;left:678px;top:40px;display:flex;gap:8px}
.badge{height:36px;border-radius:3px;color:#fff;text-align:center;padding-top:5px;font:700 12px/1.1 Arimo,Arial,sans-serif}
.badge small{display:block;font-weight:400;font-size:9px}
.badge.ship{width:112px;background:var(--orange)}
.badge.worry{width:102px;background:#c9a37a}
.badge.nz{width:114px;background:var(--plum)}
/* nav */
.nav{position:absolute;top:88px;left:0;width:1200px;height:40px;background:var(--plum)}
.nav ul{list-style:none;position:absolute;left:174px;top:9px;display:flex;gap:9px}
.nav li{height:23px;padding:0 18px;border-radius:12px;background:#fff;font:700 11px/23px Arimo,Arial,sans-serif;color:#333}
.nav li.active{background:var(--yellow)}
.search{position:absolute;left:830px;top:9px;width:196px;height:23px;border-radius:12px;background:#fff;font:12px/23px Arimo,Arial,sans-serif;color:#333;padding-left:12px}
.search i{position:absolute;right:3px;top:3px;width:17px;height:17px;border-radius:50%;background:var(--plum)}
/* hero */
.hero{position:absolute;top:128px;left:0;width:1200px;height:470px;overflow:hidden;
  background:linear-gradient(180deg,var(--tan) 0%,#c9a27c 60%,var(--tan-light) 100%)}
.hero-copy{position:absolute;left:150px;top:62px;width:540px;text-align:center;color:#fff;font-family:Arvo,Georgia,serif;white-space:nowrap}
.hero-copy .l1{font-size:36px;line-height:1.2}
.hero-copy .l2{font-size:42px;font-weight:700;line-height:1.15}
.hero-copy .l3{font-size:40px;line-height:1.15}
.hero-copy .l4{font-size:24px;font-weight:700;margin-top:8px}
.hero-figure{position:absolute;left:672px;top:4px;width:340px;height:300px;border-radius:40px 40px 0 0;
  background:linear-gradient(180deg,#a9825d,#8f6e52 60%,#6c8aa9)}
.hero-clouds{position:absolute;left:0;bottom:0;width:1200px;height:190px;
  background:linear-gradient(180deg,rgba(235,231,216,0) 0%,var(--cloud) 45%,#eeebdf 100%)}
.arrow{position:absolute;top:147px;width:44px;height:88px;background:#fff}
.arrow svg{position:absolute;top:34px;left:14px}
.arrow.prev{left:0}.arrow.next{right:0}
/* section titles */
.sec-title{position:absolute;left:172px;width:854px;text-align:center;font:700 27px Arvo,Georgia,serif;color:#111}
.sec-title::before,.sec-title::after{content:"";position:absolute;top:50%;width:var(--w);height:1px;background:#9a9a9a}
.sec-title::before{left:0}.sec-title::after{right:0}
/* product grid */
.promo{position:absolute;width:207px;height:324px;color:#fff;padding:38px 18px 0}
.promo h3{font:700 28px/1 Arvo,Georgia,serif}
.promo p{font-size:11px;line-height:1.3;margin-top:14px}
.promo.new{background:var(--plum)}
.promo.featured{background:var(--coral)}
.card{position:absolute;width:203px;height:324px;background:#fff;border:2px solid #cfd0c3}
.card.hover{border-color:var(--berry)}
.card .photo{position:absolute;left:40px;top:12px;width:120px;height:232px;border-radius:18px 18px 6px 6px}
.card .info{position:absolute;left:0;bottom:0;width:100%;height:62px;background:var(--grey-band);padding:8px 10px 0}
.card.hover .info{background:var(--plum);color:#fff}
.card .name{font-size:11px}
.card .price{font:700 14px Arimo,Arial,sans-serif;margin-top:8px}
.card .stock{position:absolute;right:0;bottom:0;height:18px;padding:0 7px;font:10px/18px Arimo,Arial,sans-serif;background:var(--stock);color:#fff}
.card.hover .stock{background:var(--yellow);color:#333}
.tag{position:absolute;left:-6px;height:20px;padding:0 10px;font:10px/20px Arimo,Arial,sans-serif;color:#fff;background:var(--berry)}
.tag.compare{background:var(--plum-dark)}
.row2 .tag{background:var(--coral)}
.row2 .tag.compare{background:var(--coral-dark)}
.row2 .card.hover{border-color:var(--coral)}
.row2 .card.hover .info{background:var(--coral)}
/* brands */
.brands{position:absolute;left:174px;top:1075px;display:flex;gap:15px}
.brands div{width:128px;height:68px;background:#fff;border:1px solid #c8c8c8;display:flex;align-items:center;justify-content:center;font:700 15px Arimo,Arial,sans-serif;color:#333;text-align:center}
.brands div.on{box-shadow:0 0 0 2px #555 inset}
/* about */
.about{position:absolute;left:174px;top:1588px;width:384px;font-size:11.4px;line-height:1.42;color:#222}
.about h4{font:700 15px Arimo,Arial,sans-serif;margin-bottom:8px}
.about p+p{margin-top:18px}
.tile{position:absolute;width:220px;height:110px;color:#fff;overflow:hidden}
.tile .disc{position:absolute;left:-50px;top:5px;width:100px;height:100px;border-radius:50%;background:#fff}
.tile svg{position:absolute;left:8px;top:37px}
.tile h5{position:absolute;left:84px;top:12px;font:700 13px Arvo,Georgia,serif}
.tile p{position:absolute;left:84px;top:32px;width:124px;font-size:10px;line-height:1.2}
/* footer */
.footer{position:absolute;left:0;top:1889px;width:1200px;height:278px;background:var(--plum);color:#fff}
.footer-mark{position:absolute;left:548px;top:1858px;width:104px;height:104px;border-radius:50%;background:#fff}
.fcol{position:absolute;top:93px}
.fcol h6{font:700 13px Arvo,Georgia,serif;letter-spacing:.5px;margin-bottom:12px}
.fcol li{list-style:none;font-size:11px;line-height:20px}
.news{position:absolute;left:815px;top:2012px;width:210px;height:26px;background:#fff}
.news i{position:absolute;right:0;top:0;width:26px;height:26px;background:var(--yellow)}
.social{position:absolute;left:815px;top:2080px;display:flex;gap:6px}
.social i{width:20px;height:20px;border-radius:50%;background:var(--amber)}
.copy{position:absolute;top:236px;left:0;width:1200px;text-align:center;font-size:11px;color:#fff}
.to-top{position:absolute;left:1080px;top:2005px;width:64px;height:64px;border-radius:50%;background:var(--red-pink);box-shadow:0 3px 6px rgba(0,0,0,.3)}
</style>
</head>
<body>
<div class="header">
  <div class="edge-band" style="top:0" role="img" aria-label="Multicoloured striped border"></div>
  <div class="brand">
    <div class="brand-dot"></div>
    <div><div class="brand-name">Kids Costumes</div><div class="brand-tag">Your company slogan goes here</div></div>
  </div>
  <div class="top-links"><span>MY ACCOUNT</span><span>WISHLIST</span><span>MY CART</span><span>CHECKOUT</span><span>LOG IN</span></div>
  <div class="badges">
    <div class="badge ship">Free shipping<small>on all orders over $50</small></div>
    <div class="badge worry">Worry free<small>Return policy</small></div>
    <div class="badge nz">100% NZ owned<small>*Conditions Apply</small></div>
  </div>
</div>

<nav class="nav">
  <ul><li class="active">HOME</li><li>TODDLERS</li><li>GIRLS</li><li>BOYS</li><li>ACCESSORIES</li><li>THEMES</li></ul>
  <div class="search">Enter your search<i></i></div>
</nav>

<section class="hero">
  <div class="hero-figure" role="img" aria-label="Cartoon shop assistant holding a fan of banknotes"></div>
  <div class="hero-clouds" role="img" aria-label="Illustrated band of soft clouds"></div>
  <div class="hero-copy">
    <div class="l1">Don’t love it</div>
    <div class="l2">WORRY FREE RETURNS</div>
    <div class="l3">return it fast and easy</div>
    <div class="l4">with our free return label</div>
  </div>
  <div class="arrow prev"><svg width="14" height="20"><path d="M12 2 4 10l8 8" stroke="#111" stroke-width="4" fill="none"/></svg></div>
  <div class="arrow next"><svg width="14" height="20"><path d="M2 2l8 8-8 8" stroke="#111" stroke-width="4" fill="none"/></svg></div>
</section>

<h2 class="sec-title" style="top:628px;--w:280px">KIDS COSTUME</h2>

<div class="promo new" style="left:174px;top:678px"><h3>NEW<br>PRODUCTS</h3><p>Neque porro quisquam est, qui dolorem ipsum quia dolor sit amet, consectetur, adipisci velit, sed quia non numquam eius modi tempora incidunt ut labore et dolore magnam aliquam quaerat voluptatem.</p></div>

<div class="card hover" style="left:396px;top:678px">
  <div class="photo" role="img" aria-label="Child in a black ninja costume with sword" style="background:linear-gradient(180deg,#3a3a3a,#1b1b1b)"></div>
  <span class="tag" style="top:172px">Add to wishlist</span><span class="tag compare" style="top:204px">Add to compare</span>
  <div class="info"><div class="name">Bolt Ranger Deluxe Boys Costume</div><div class="price">NZ$59.99</div><span class="stock">Out of stock</span></div>
</div>
<div class="card" style="left:611px;top:678px">
  <div class="photo" role="img" aria-label="Child in a purple ringmaster costume with top hat" style="background:linear-gradient(180deg,#4a3550,#2a2a33)"></div>
  <span class="tag" style="top:172px">Add to wishlist</span><span class="tag compare" style="top:204px">Add to compare</span>
  <div class="info"><div class="name">Bolt Ranger Deluxe Boys Costume</div><div class="price">NZ$59.99</div><span class="stock">Out of stock</span></div>
</div>
<div class="card" style="left:826px;top:678px">
  <div class="photo" role="img" aria-label="Child in a red and blue superhero suit" style="background:linear-gradient(180deg,#c8262f,#2d4c9a)"></div>
  <span class="tag" style="top:172px">Add to wishlist</span><span class="tag compare" style="top:204px">Add to compare</span>
  <div class="info"><div class="name">Bolt Ranger Deluxe Boys Costume</div><div class="price">NZ$59.99</div><span class="stock">Out of stock</span></div>
</div>

<h2 class="sec-title" style="top:1020px;--w:260px">POPULAR BRANDS</h2>
<div class="brands">
  <div class="on">Duskwing</div><div>Starlit</div><div>Lost Lad</div><div>Looking Glass</div><div>Wand Academy</div><div>Seven Seas Tales</div>
</div>

<div class="row2">
  <div class="card hover" style="left:176px;top:1191px">
    <div class="photo" role="img" aria-label="Child in a vampire costume with red cape" style="background:linear-gradient(180deg,#6d1f2a,#2b1d22)"></div>
    <span class="tag" style="top:172px">Add to wishlist</span><span class="tag compare" style="top:204px">Add to compare</span>
    <div class="info"><div class="name">Bolt Ranger Deluxe Boys Costume</div><div class="price">NZ$59.99</div><span class="stock">Out of stock</span></div>
  </div>
  <div class="card" style="left:391px;top:1191px">
    <div class="photo" role="img" aria-label="Child in a green muscle hero costume" style="background:linear-gradient(180deg,#4f6b55,#2f4766)"></div>
    <span class="tag" style="top:172px">Add to wishlist</span><span class="tag compare" style="top:204px">Add to compare</span>
    <div class="info"><div class="name">Bolt Ranger Deluxe Boys Costume</div><div class="price">NZ$59.99</div><span class="stock">Out of stock</span></div>
  </div>
  <div class="card" style="left:606px;top:1191px">
    <div class="photo" role="img" aria-label="Child in a caped thunder warrior costume holding a hammer" style="background:linear-gradient(180deg,#5a5e66,#8a2230)"></div>
    <span class="tag" style="top:172px">Add to wishlist</span><span class="tag compare" style="top:204px">Add to compare</span>
    <div class="info"><div class="name">Bolt Ranger Deluxe Boys Costume</div><div class="price">NZ$59.99</div><span class="stock">Out of stock</span></div>
  </div>
  <div class="promo featured" style="left:819px;top:1191px"><h3>FEATURED<br>PRODUCTS</h3><p>Neque porro quisquam est, qui dolorem ipsum quia dolor sit amet, consectetur, adipisci velit, sed quia non numquam eius modi tempora incidunt ut labore et dolore magnam aliquam quaerat voluptatem.</p></div>
</div>

<h2 class="sec-title" style="top:1533px;--w:220px">ABOUT KIDS COSTUMES</h2>
<div class="about">
  <h4>Quis autem vel eum iure reprehenderit qui</h4>
  <p>Lorem ipsum dolor sit amet, consectetur adipisicing elit, sed do eiusmod tempor incididunt ut labore et dolore magna aliqua. Ut enim ad minim veniam, quis nostrud exercitation ullamco laboris nisi ut aliquip ex ea commodo consequat. Duis aute irure dolor in reprehenderit in voluptate velit esse cillum dolore eu fugiat nulla pariatur. Excepteur sint occaecat cupidatat non proident, sunt in culpa qui officia.</p>
  <p>Lorem ipsum dolor sit amet, consectetur adipisicing elit, sed do eiusmod tempor incididunt ut labore et dolore magna aliqua. Ut enim ad minim veniam, quis nostrud exercitation ullamco laboris nisi ut aliquip ex ea commodo consequat. Duis aute irure dolor in reprehenderit in voluptate velit esse cillum dolore eu fugiat nulla pariatur. Excepteur sint occaecat cupidatat non proident, sunt in culpa qui officia.</p>
</div>

<div class="tile" style="left:570px;top:1590px;background:var(--coral)"><span class="disc"></span>
  <svg width="36" height="36" viewBox="0 0 36 36"><circle cx="18" cy="18" r="11" fill="none" stroke="#ef5a5c" stroke-width="7" stroke-dasharray="5 3"/><circle cx="18" cy="18" r="5" fill="#ef5a5c"/></svg>
  <h5>ACCESSORIES</h5><p>Neque porro quisquam est, qui dolorem ipsum quia dolor sit amet, consectetur, adipisci velit, sed quia.</p></div>
<div class="tile" style="left:806px;top:1590px;background:var(--orange)"><span class="disc"></span>
  <svg width="36" height="36" viewBox="0 0 36 36"><path d="M3 7h6l4 16h16l4-12H12" fill="none" stroke="#f7931e" stroke-width="3"/><circle cx="15" cy="29" r="3" fill="#f7931e"/><circle cx="27" cy="29" r="3" fill="#f7931e"/></svg>
  <h5>FREE SHIPPING</h5><p>Neque porro quisquam est, qui dolorem ipsum quia dolor sit amet, consectetur, adipisci velit, sed quia.</p></div>
<div class="tile" style="left:570px;top:1713px;background:var(--red-pink)"><span class="disc"></span>
  <svg width="36" height="36" viewBox="0 0 36 36"><path d="M4 14h7l14-8v24l-14-8H4z" fill="#ee3b5b"/><path d="M9 22l3 9h4l-2-9" fill="#ee3b5b"/></svg>
  <h5>NEW ARRIVALS</h5><p>Neque porro quisquam est, qui dolorem ipsum quia dolor sit amet, consectetur, adipisci velit, sed quia.</p></div>
<div class="tile" style="left:806px;top:1713px;background:var(--amber)"><span class="disc"></span>
  <svg width="36" height="36" viewBox="0 0 36 36"><path d="M30 15A12 12 0 0 0 8 11M6 21a12 12 0 0 0 22 4" fill="none" stroke="#fbb116" stroke-width="4"/><path d="M4 6v8h8z M32 30v-8h-8z" fill="#fbb116"/></svg>
  <h5>WORRY FREE</h5><p>Neque porro quisquam est, qui dolorem ipsum quia dolor sit amet, consectetur, adipisci velit, sed quia.</p></div>

<footer class="footer">
  <div class="fcol" style="left:174px"><h6>KIDS COSTUMES</h6><ul><li>About Us</li><li>Contact Us</li><li>Advanced Search</li><li>Terms &amp; Conditions</li><li>Sitemap</li></ul></div>
  <div class="fcol" style="left:383px"><h6>CUSTOMER SERVICE</h6><ul><li>Shipping &amp; Delivery</li><li>Returns Policy</li><li>Sizing Guide</li><li>Contact Us</li></ul></div>
  <div class="fcol" style="left:625px"><h6>MY ACCOUNT</h6><ul><li>My Account</li><li>Order History</li><li>Wish List</li><li>Compare</li></ul></div>
  <div class="fcol" style="left:815px"><h6>OUR NEWSLETTER</h6></div>
  <div class="fcol" style="left:815px;top:163px"><h6>FOLLOW US ON</h6></div>
  <div class="copy">© 2012 Harbourline Store. All Rights Reserved.</div>
  <div class="edge-band" style="bottom:0" role="img" aria-label="Multicoloured striped border"></div>
</footer>
<div class="footer-mark"></div>
<div class="news"><i></i></div>
<div class="social"><i></i><i></i><i></i><i></i><i></i></div>
<div class="to-top"><svg width="64" height="64"><path d="M32 22v20M24 30l8-8 8 8" stroke="#fff" stroke-width="3" fill="none"/></svg></div>
</body>
</html>
```